Harbouring Stillwave Inc needs a business card design

Looking for a unique, classy and sharp business card design.

Contact Information for Business Card

Harbouring Stillwave Inc.
Nadia Ferreira Quintanilla BScOT(c)
Occupational Therapist
(780) 555-0142
harbouringstillwave@mailvora.com

```html
<!DOCTYPE html>
<html lang="en">
<head>
<meta charset="utf-8">
<title>Harbouring Stillwave Inc – Business Card</title>
<link rel="stylesheet" href="https://fonts.googleapis.com/css2?family=Roboto:wght@400;500;700&family=Roboto+Condensed:wght@700&display=swap">
<style>
  :root {
    --bg: #e9e9ec;
    --lime: #86c13b;
    --lime-light: #b9e05a;
    --purple: #9a2c9c;
    --sky: #2aa6d8;
    --paper: #ffffff;
    --ink-white: #ffffff;
  }
  * { box-sizing: border-box; margin: 0; padding: 0; }
  html, body { width: 1200px; height: 886px; overflow: hidden; }
  body {
    background: var(--bg);
    font-family: "Roboto", Arial, sans-serif;
    display: flex;
    flex-direction: column;
    align-items: center;
    justify-content: center;
    gap: 60px;
  }
  .card {
    position: relative;
    width: 600px;
    height: 343px;
    border-radius: 22px;
    overflow: hidden;
    box-shadow: 0 6px 18px rgba(0,0,0,0.18);
  }
  /* Front */
  .card-front {
    background: var(--lime);
    color: var(--ink-white);
    display: flex;
    flex-direction: column;
    align-items: center;
    justify-content: center;
  }
  .brand {
    display: flex;
    align-items: center;
    gap: 12px;
    font-weight: 700;
    font-size: 40px;
    letter-spacing: -0.5px;
    white-space: nowrap;
  }
  .brand-dot {
    width: 26px; height: 26px;
    border-radius: 50%;
    background: currentColor;
    flex: none;
  }
  .front-web {
    position: absolute;
    bottom: 52px;
    font-size: 13px;
    letter-spacing: 5px;
  }
  /* Back */
  .card-back { background: var(--paper); }
  .card-back .wave { position: absolute; inset: 0; }
  .back-brand {
    position: absolute;
    left: 30px;
    top: 96px;
    color: var(--purple);
    font-size: 24px;
    gap: 9px;
  }
  .back-brand .brand-dot { width: 16px; height: 16px; background: var(--lime); }
  .contact {
    position: absolute;
    right: 26px;
    top: 132px;
    text-align: right;
    color: var(--ink-white);
    line-height: 1.4;
    white-space: nowrap;
  }
  .contact-name {
    font-family: "Roboto Condensed", "Arial Narrow", sans-serif;
    font-weight: 700;
    font-size: 14px;
    color: var(--lime-light);
  }
  .contact-role { font-weight: 700; font-size: 13px; }
  .contact-company { font-size: 13px; margin-bottom: 10px; }
  .contact-line {
    font-size: 13px;
    display: flex;
    align-items: center;
    justify-content: flex-end;
    gap: 7px;
  }
  .contact-line svg { width: 12px; height: 12px; fill: var(--ink-white); flex: none; }
</style>
</head>
<body>

<section class="card card-front">
  <div class="brand"><span class="brand-dot"></span>Harbouring Stillwave</div>
  <p class="front-web">www.harbouringstillwave.com</p>
</section>

<section class="card card-back">
  <svg class="wave" viewBox="0 0 600 343" preserveAspectRatio="none" aria-hidden="true">
    <path d="M0,262 C220,272 270,236 320,126 C370,30 450,18 600,12 L600,343 L0,343 Z" fill="var(--sky)"/>
    <path d="M0,270 C220,280 270,244 320,134 C370,38 450,26 600,20 L600,343 L0,343 Z" fill="var(--paper)"/>
    <path d="M0,274 C222,284 274,250 324,140 C374,46 452,32 600,26 L600,343 L0,343 Z" fill="var(--lime)"/>
    <path d="M0,288 C222,296 280,262 334,150 C384,58 460,42 600,38 L600,343 L0,343 Z" fill="var(--purple)"/>
  </svg>

  <div class="brand back-brand"><span class="brand-dot"></span>Harbouring Stillwave</div>

  <div class="contact">
    <p class="contact-name">Nadia Ferreira Quintanilla BScOT(c)</p>
    <p class="contact-role">Occupational Therapist</p>
    <p class="contact-company">Harbouring Stillwave Inc.</p>
    <p class="contact-line">(780) 555-0142
      <svg viewBox="0 0 24 24"><path d="M6.6 10.8a15.1 15.1 0 0 0 6.6 6.6l2.2-2.2a1 1 0 0 1 1-.25 11.4 11.4 0 0 0 3.6.57 1 1 0 0 1 1 1V20a1 1 0 0 1-1 1A17 17 0 0 1 3 4a1 1 0 0 1 1-1h3.5a1 1 0 0 1 1 1c0 1.25.2 2.45.57 3.57a1 1 0 0 1-.25 1z"/></svg>
    </p>
    <p class="contact-line">harbouringstillwave@mailvora.com
      <svg viewBox="0 0 24 24"><path d="M2 5h20v14H2z M2 5l10 8 10-8" fill="var(--ink-white)" stroke="var(--purple)" stroke-width="1.6"/></svg>
    </p>
    <p class="contact-line">www.harbouringstillwave.com
      <svg viewBox="0 0 24 24"><circle cx="12" cy="12" r="10"/></svg>
    </p>
  </div>
</section>

</body>
</html>
```